New Business Card

We need to refresh our business cards. We designed these ourselves and we have no graphic design experience. We would like to find a new business card design that is professional and unique. We are an auto finance company. Feel free to play with the logo, but we would like to keep the eye very present on the card. Our corporate colors are green, grey, and white.
Green - RGB - 168,215,27; HEX - #AADD22
Grey - RGB - 196,196,196; HEX - #C4C4C4
Updates
Need to upload the vector file to finalize the project. The last logo was for a jpeg that didn't stretch well.
Industry/Entity Type
Financial Service
Contact Information for Business Card
Honestly don't know...I need your help!

```html
<!DOCTYPE html>
<html lang="en">
<head>
<meta charset="utf-8">
<title>Brightlane Capital – Business Card</title>
<link rel="stylesheet" href="https://fonts.googleapis.com/css2?family=Gelasio:wght@400;700&display=swap">
<style>
  :root {
    --panel-edge: #9fb0ae;
    --panel-center: #c3cdcc;
    --paper: #f6f7f6;
    --paper-center: #ffffff;
    --ink-light: #ffffff;
    --brand-green: #a4ff00;
    --brand-grey: #b9c4c2;
  }
  * { box-sizing: border-box; margin: 0; padding: 0; }
  html, body {
    width: 1200px; height: 720px; overflow: hidden;
    background: var(--paper);
  }
  .card {
    position: relative;
    width: 1200px; height: 720px;
    display: flex;
    font-family: "Gelasio", Georgia, serif;
  }
  .identity-panel {
    width: 627px; height: 720px;
    background: radial-gradient(ellipse at 55% 50%, var(--panel-center) 0%, var(--panel-edge) 85%);
    color: var(--ink-light);
    position: relative;
  }
  .company-name {
    position: absolute; left: 0; width: 672px;
    top: 132px;
    text-align: center;
    font-weight: 400;
    line-height: 1;
  }
  .company-name .primary { display: block; font-size: 84px; }
  .company-name .secondary {
    display: block; font-size: 34px; letter-spacing: 30px;
    margin-top: 26px; padding-left: 30px; text-transform: uppercase;
  }
  .person {
    position: absolute; left: 0; width: 672px; top: 328px;
    text-align: center;
  }
  .person-name {
    display: inline-block;
    font-size: 62px; font-weight: 400; line-height: 1.1;
    border-bottom: 2px solid var(--ink-light);
    padding: 0 2px 2px;
  }
  .person-role { font-size: 31px; font-weight: 400; margin-top: 6px; }
  .contact-list {
    position: absolute; left: 205px; top: 447px;
    list-style: none;
  }
  .contact-item {
    display: flex; align-items: center;
    height: 49px;
    font-size: 22px; font-weight: 700;
  }
  .contact-icon { width: 32px; height: 30px; margin-right: 14px; flex: none; }
  .contact-icon svg { width: 100%; height: 100%; display: block; fill: var(--ink-light); }

  .brand-panel {
    flex: 1; height: 720px;
    background: radial-gradient(ellipse at 50% 50%, var(--paper-center) 0%, var(--paper) 80%);
    display: flex; align-items: center; justify-content: center;
  }
  .brand-mark {
    display: flex; align-items: center; gap: 22px;
    margin-top: -20px;
  }
  .brand-dot {
    width: 96px; height: 96px; border-radius: 50%;
    background: var(--brand-green);
  }
  .brand-word {
    font-size: 58px; font-weight: 400; color: var(--brand-grey);
  }
</style>
</head>
<body>
<main class="card">
  <section class="identity-panel">
    <h1 class="company-name">
      <span class="primary">Brightlane</span>
      <span class="secondary">Capital</span>
    </h1>
    <div class="person">
      <p class="person-name">Daniel Hart</p>
      <p class="person-role">President</p>
    </div>
    <ul class="contact-list">
      <li class="contact-item">
        <span class="contact-icon"><svg viewBox="0 0 32 30" aria-hidden="true"><path d="M10 1h12a2 2 0 0 1 2 2v24a2 2 0 0 1-2 2H10a2 2 0 0 1-2-2V3a2 2 0 0 1 2-2zm0 3v19h12V4zm6 21a1.5 1.5 0 1 0 0 3a1.5 1.5 0 0 0 0-3z"/></svg></span>
        000-000-0000
      </li>
      <li class="contact-item">
        <span class="contact-icon"><svg viewBox="0 0 32 30" aria-hidden="true"><path d="M5 3l5-2 4 8-3 3c2 4 5 7 9 9l3-3 8 4-2 5c-1 2-4 2-6 1C13 25 7 19 3 9 2 7 3 4 5 3z"/></svg></span>
        888-555-0142
      </li>
      <li class="contact-item">
        <span class="contact-icon"><svg viewBox="0 0 32 30" aria-hidden="true"><path d="M2 6h28v18H2zm2.5 2l11.5 9 11.5-9v1.5L16 19 4.5 9.5zm0 14h23l-8-7-1 1 7 5.5h-20l7-5.5-1-1z" fill-rule="evenodd"/></svg></span>
        daniel@brightlane.com
      </li>
      <li class="contact-item">
        <span class="contact-icon"><svg viewBox="0 0 32 30" aria-hidden="true"><path d="M16 2a13 13 0 1 0 0 26a13 13 0 0 0 0-26zm-5 4c2 1 4 3 3 5s-4 1-5 3 1 4 0 6-3 1-4-2C4 13 7 8 11 6zm9 3c3 0 6 3 6 7s-2 8-5 9c-1-2 1-4 0-6s-3-1-3-4 0-5 2-6z"/></svg></span>
        brightlane.com
      </li>
    </ul>
  </section>
  <section class="brand-panel">
    <div class="brand-mark">
      <span class="brand-dot"></span>
      <span class="brand-word">Brightlane</span>
    </div>
  </section>
</main>
</body>
</html>
```